webdesign for a spectacles/glasses designer

Hello,

Someone in my village designs his own spectacles/eyeglasses.

For this I need a design that looks better than my poor design skills ;o)

The site is based around collections, subcollections and the actual items.

So we need a design that lists these in a nice way, worst case on seperate pages.

Here you can find the working material...

https://www.filevaultic.com/s/q7kmtr4p2wz91xb/BriefHarbor.zip

keep an eye on the product_tree file.

first level is the collection name
2nd is the model group
3rd is the model (on most of them it's just a different color of the same base model)

I added a seperate contact info file (line is too slow to reupload 60Mb again :( )

https://dl.filevaulticcontent.com/u/31906524/Anselm/contact.zip

I think I forgot to mention that it will be a shop like site to present his products,
altho I will add a cart system there won't be a payment system linked to it as
people who place orders will get contacted with payment instructions.
Updates

In the zipfile /Logo/logo_mistral_font.psd is the main logo
(you need to change character spacing to 1 to get rid of the spacing gaps)

the other one is only a collection logo

Target Market(s)

Plain customers and his resellers.

Industry/Entity Type

Shop

Requirements
Must have
• - a design that suits responsive behaviour (via the 960 grid)
- a menu is always handy (home, about, collections, contact)
- highlighted area/slider to highlight his sunglasses over glasses thingy
- featured products (newly added or promotional stuff)

there is a lot of pretty pictures to be supplied so do what you think is best

Nice to have
• a roll over zoom with selectable thumbnails or a plain gallery with full picture display at the product page.

maybe a drop down menu for the collection part (I will supply a screenshot of the backend structure)

```html
<!DOCTYPE html>
<html lang="en">
<head>
<meta charset="utf-8">
<title>Anselm Eyewear</title>
<link rel="stylesheet" href="https://fonts.googleapis.com/css2?family=Roboto:wght@300;400;500;700&family=Roboto+Condensed:wght@400;700&family=Roboto+Slab:wght@700&display=swap">
<style>
:root{
  --ink:#1b1b1b;
  --muted:#666;
  --pink:#e8315a;
  --red:#e21f26;
  --green:#5cb531;
  --footer:#242424;
  --footer-text:#8a8a8a;
  --panel:#e3e3e3;
  --blue-soft:#a8e2f5;
  --yellow:#f4e44a;
}
*{margin:0;padding:0;box-sizing:border-box}
html,body{width:859px;height:1200px;overflow:hidden}
body{position:relative;background:#fff;font-family:"Roboto",Arial,sans-serif;color:var(--ink)}
.abs{position:absolute}

/* header */
.site-header{left:0;top:0;width:859px;height:88px;background:linear-gradient(#fff,#f1f1f1)}
.brand{left:24px;top:14px;font-size:46px;font-weight:400;color:#111;letter-spacing:1px;line-height:60px}
.top-links{top:21px;display:flex;align-items:center;gap:5px;font-size:9px;font-weight:500;color:#333}
.top-links svg{width:16px;height:14px}
.search{left:403px;top:52px;width:162px;height:17px;border:1px solid #bbb;background:#fff;font-size:8px;color:#777;padding:3px 6px}
.search-btn{left:571px;top:53px;width:15px;height:15px;background:var(--green);border-radius:2px}
.phone{left:599px;top:48px;font-size:19px;font-weight:300;color:#333}

/* nav */
.main-nav{left:0;top:88px;width:859px;height:40px;background:linear-gradient(#f7f7f7,#e9e9e9);border-top:1px solid #ddd;border-bottom:1px solid #d3d3d3}
.main-nav ul{position:absolute;left:37px;top:0;display:flex;list-style:none;height:40px;background:#f6f6f6;box-shadow:0 0 3px rgba(0,0,0,.12)}
.main-nav li{height:40px;display:flex;align-items:center;justify-content:center;font-family:"Roboto Condensed",Arial,sans-serif;font-size:10px;color:#333;border-right:1px solid #e0e0e0}

/* hero */
.hero{left:0;top:128px;width:859px;height:297px}
.hero-photo{left:0;top:0;width:453px;height:297px;background:radial-gradient(circle at 40% 45%,#b9a99a 0,#8d8d8d 35%,#6e6e6e 100%)}
.hero-side{left:453px;top:0;width:406px;height:297px;background:linear-gradient(120deg,#9a9a9a 0,#7d2530 35%,#b9b9b9 60%,#5f5f5f 100%)}
.hero-title{left:486px;top:52px;font-size:41px;font-weight:700;letter-spacing:.5px;color:#fff}
.hero-title span{color:var(--pink)}
.badge{left:486px;top:114px;width:64px;height:64px;border-radius:50%;background:var(--pink);color:#fff;text-align:center;font-size:17px;line-height:17px;padding-top:14px;box-shadow:0 2px 5px rgba(0,0,0,.3)}
.badge small{display:block;font-size:16px;font-weight:300}
.hero-tag{left:567px;top:117px;font-size:26px;font-weight:500;line-height:27px;color:#fff}
.shop-now{left:496px;top:208px;display:flex;align-items:center;gap:4px;font-size:10.5px;font-weight:500;color:#111}
.hero-arrows{left:418px;top:265px;display:flex;gap:30px}

/* frames */
.frames{left:0;top:425px;width:859px;height:266px;background:#fafafa}
.frames-title{left:0;top:17px;width:859px;display:flex;align-items:center;justify-content:center;gap:14px;font-size:22px;font-weight:300;letter-spacing:.8px;color:#555;line-height:30px}
.frames-title::before,.frames-title::after{content:"";width:67px;height:1px;background:#999}
.shape-picker{left:175px;top:60px;display:flex;gap:19px}
.shape-picker i{display:block;width:48px;height:48px;border-radius:50%;border:2px solid #e6e6e6;background:linear-gradient(135deg,#fff 30%,#b33a48 50%,#fff 70%)}
.pointer{left:525px;top:113px}
.thumbs{left:113px;top:138px;display:flex;gap:12px}
.thumbs div{width:109px;height:109px;border:1px solid #ddd;box-shadow:0 1px 3px rgba(0,0,0,.2)}

/* promos */
.promos{left:0;top:691px;width:859px;height:318px;background:var(--panel)}
.tile{position:absolute;width:201px;height:131px;overflow:hidden;color:#fff}
.t1{left:107px;top:25px;background:linear-gradient(150deg,#fafafa 0,#cfcfcf 30%,#1d1d1d 55%,#3a3a3a 100%)}
.t1 .band{position:absolute;left:0;bottom:0;width:100%;height:54px;background:rgba(70,70,70,.82);padding:6px 9px}
.t1 b{display:block;font-size:21px;font-weight:300}
.t1 em{font-style:normal;font-size:11.5px;font-weight:300;color:#ddd}
.t2{left:329px;top:25px;background:linear-gradient(#6e6e6e,#9a8c80 60%,#555)}
.t2 .band{position:absolute;left:0;bottom:0;width:100%;height:27px;background:#111;display:flex;align-items:center;justify-content:space-between;padding:0 10px 0 11px;font-size:11.5px;font-weight:500}
.t2 .ribbon{position:absolute;left:0;top:0}
.t3{left:550px;top:25px;background:linear-gradient(#cfcfcf,#e2e2e2 40%,#5a2a2a 75%,#d8d8d8)}
.t3 .band{height:40px;background:rgba(110,110,110,.9);padding:5px 8px;font-size:12px;font-weight:300;line-height:12px}
.t4{left:107px;top:170px;background:#fff}
.t4 .photo{position:absolute;left:0;top:0;width:117px;height:131px;background:linear-gradient(#d9c7b0,#8a7565 60%,#4a4040)}
.t4 .mark{position:absolute;left:125px;top:9px;font-size:25px;color:#111}
.t4 .panel{position:absolute;left:117px;top:55px;width:84px;height:76px;background:var(--blue-soft);color:#333;padding:6px 10px;font-size:11.5px;line-height:14px}
.t4 .panel b{font-weight:700}
.t5{left:329px;top:170px;background:linear-gradient(125deg,#2b2b2b,#6b6b6b 50%,#3a3a3a)}
.t5 .inner{position:absolute;left:16px;top:26px}
.t5 h3{font-family:"Roboto Slab",Georgia,serif;font-size:16px;letter-spacing:.5px}
.t5 .sub{color:var(--yellow);font-size:14px;font-weight:400}
.t5 p{font-size:10px;margin-top:3px}
.t5 .btn{display:inline-block;margin-top:7px;background:var(--pink);font-size:11px;font-weight:500;padding:3px 14px}
.t6{left:550px;top:170px;background:var(--red)}
.t6 .flat{position:absolute;left:130px;top:8px;font-size:9px;font-weight:700;letter-spacing:1px;line-height:10px}
.t6 .offer{position:absolute;left:106px;top:19px;display:flex;align-items:flex-start;gap:2px}
.t6 .num{font-size:40px;font-weight:300;line-height:36px}
.t6 .stack{display:flex;flex-direction:column;align-items:center;padding-top:2px}
.t6 .pc{font-size:20px;font-weight:300;line-height:19px}
.t6 .off{font-size:12px;font-weight:300;line-height:13px}
.t6 .word{position:absolute;left:13px;top:56px;font-size:60px;font-weight:700;letter-spacing:-2px;line-height:60px}
.t6 .days{position:absolute;left:85px;top:118px;font-size:8.5px;letter-spacing:.5px;line-height:10px}

/* footer */
.site-footer{left:0;top:1009px;width:859px;height:191px;background:var(--footer)}
.footer-h{font-family:"Roboto Condensed",Arial,sans-serif;font-size:14.5px;font-weight:400;color:#eee}
.footer-links{list-style:none;font-size:8.5px;line-height:12.3px;color:var(--footer-text)}
.social{left:212px;top:53px;display:flex;gap:7px}
.social i{display:block;width:23px;height:23px;background:#c6232f}
.email{left:209px;top:119px;width:144px;height:20px;background:#fff;font-size:8.5px;color:#222;padding:5px 6px}
.submit{left:356px;top:119px;width:47px;height:20px;background:#c6232f;color:#fff;font-size:8.5px;text-align:center;line-height:20px}
.map{left:462px;top:25px;width:326px;height:111px;background:linear-gradient(135deg,#ecebe6,#dcdad2);border:2px solid #fff}
.footer-rule{left:51px;top:154px;width:752px;height:1px;background:#3c3c3c}
.copyright{left:0;top:168px;width:859px;text-align:center;font-size:8.5px;color:#777}
</style>
</head>
<body>

<header class="site-header abs">
  <div class="brand abs">Anselm</div>
  <div class="top-links abs" style="left:470px">
    <svg viewBox="0 0 16 14"><path d="M1 2h3l2 7h8l1-5H5" fill="none" stroke="#999" stroke-width="1.5"/><circle cx="7" cy="12" r="1.3" fill="#999"/><circle cx="13" cy="12" r="1.3" fill="#999"/></svg>Shopping cart
  </div>
  <div class="top-links abs" style="left:574px">
    <svg viewBox="0 0 16 14"><path d="M1 2h3l2 7h8l1-5H5" fill="none" stroke="#999" stroke-width="1.5"/><circle cx="7" cy="12" r="1.3" fill="#999"/><circle cx="13" cy="12" r="1.3" fill="#999"/></svg>Checkout
  </div>
  <div class="top-links abs" style="left:657px">
    <svg viewBox="0 0 16 14"><circle cx="11" cy="4" r="3" fill="none" stroke="#999" stroke-width="1.6"/><path d="M9 6 2 13M4 11l2 2" stroke="#999" stroke-width="1.6"/></svg>Login
  </div>
  <div class="top-links abs" style="left:724px">
    <svg viewBox="0 0 16 14"><rect x="1" y="0" width="14" height="14" fill="#aaa"/><circle cx="8" cy="5" r="2.5" fill="#fff"/><path d="M3 13c1-4 9-4 10 0z" fill="#fff"/></svg>Create an account
  </div>
  <div class="search abs">Search Keyword</div>
  <div class="search-btn abs"><svg viewBox="0 0 15 15" width="15" height="15"><circle cx="6.5" cy="6.5" r="3" fill="none" stroke="#fff" stroke-width="1.5"/><path d="M9 9l3 3" stroke="#fff" stroke-width="1.8"/></svg></div>
  <div class="phone abs">Call us +32(0)41.70.58.19</div>
</header>

<nav class="main-nav abs">
  <ul>
    <li style="width:71px">HOME</li>
    <li style="width:88px">COMPANY</li>
    <li style="width:108px">COLLECTIONS</li>
    <li style="width:84px">GLASSES</li>
    <li style="width:76px">SORTE</li>
    <li style="width:85px">BLOG</li>
    <li style="width:85px">CONTACT</li>
    <li style="width:103px">NEWSLETTER</li>
    <li style="width:83px;border-right:0">MAP</li>
  </ul>
</nav>

<section class="hero abs">
  <div class="hero-photo abs" role="img" aria-label="Model holding up two pairs of spectacle frames"></div>
  <div class="hero-side abs" role="img" aria-label="Close-up of a red spectacle frame"></div>
  <div class="hero-title abs"><span>STYLE</span>ALERT</div>
  <div class="badge abs">Look<small>Good</small></div>
  <div class="hero-tag abs">BE THE ONE<br>STAND OUT</div>
  <div class="shop-now abs">SHOP NOW
    <svg width="13" height="13" viewBox="0 0 13 13"><circle cx="6.5" cy="6.5" r="6.5" fill="#111"/><path d="M5 3.5 8 6.5 5 9.5" fill="none" stroke="#fff" stroke-width="1.6"/></svg>
  </div>
  <div class="hero-arrows abs">
    <svg width="18" height="12" viewBox="0 0 18 12"><path d="M0 6 7 0v4h11v4H7v4z" fill="#eee"/></svg>
    <svg width="18" height="12" viewBox="0 0 18 12"><path d="M18 6 11 0v4H0v4h11v4z" fill="#eee"/></svg>
  </div>
</section>

<section class="frames abs">
  <h2 class="frames-title abs">CHOOSE YOUR FRAME</h2>
  <div class="shape-picker abs" role="img" aria-label="Frame style selector with seven frame samples">
    <i></i><i></i><i></i><i></i><i></i><i></i><i></i>
  </div>
  <svg class="pointer abs" width="18" height="10" viewBox="0 0 18 10"><path d="M0 0h18L9 10z" fill="#888"/></svg>
  <svg class="abs" style="left:91px;top:187px" width="8" height="14" viewBox="0 0 8 14"><path d="M7 1 1 7l6 6" fill="none" stroke="#999" stroke-width="1.2"/></svg>
  <div class="thumbs abs">
    <div role="img" aria-label="Orange frame temple" style="background:linear-gradient(135deg,#fff 30%,#e0a060 50%,#fff 75%)"></div>
    <div role="img" aria-label="Red frame temple" style="background:linear-gradient(135deg,#fff 30%,#c8302e 50%,#fff 75%)"></div>
    <div role="img" aria-label="Brown metal frame temple" style="background:linear-gradient(135deg,#fff 30%,#7a5a48 50%,#fff 75%)"></div>
    <div role="img" aria-label="Blue rimless frame" style="background:linear-gradient(135deg,#fff 35%,#6a6ad8 50%,#fff 65%)"></div>
    <div role="img" aria-label="Purple frame temple" style="background:linear-gradient(135deg,#fff 30%,#4a3ab8 50%,#fff 75%)"></div>
  </div>
  <svg class="abs" style="left:716px;top:187px" width="8" height="14" viewBox="0 0 8 14"><path d="M1 1l6 6-6 6" fill="none" stroke="#999" stroke-width="1.2"/></svg>
</section>

<section class="promos abs">
  <div class="tile t1" role="img" aria-label="Black frame close-up">
    <div class="band"><b>The Lightest</b><em>Eyewear for every Occasion</em></div>
  </div>
  <div class="tile t2" role="img" aria-label="Model wearing dark sunglasses">
    <svg class="ribbon" width="34" height="34" viewBox="0 0 34 34"><path d="M0 0h34L0 34z" fill="#e8315a"/><text x="4" y="19" transform="rotate(-45 10 14)" font-family="Roboto,Arial,sans-serif" font-size="7" font-weight="700" fill="#fff">NEW</text></svg>
    <div class="band">NEW ARRIVALS
      <svg width="13" height="13" viewBox="0 0 13 13"><circle cx="6.5" cy="6.5" r="6.5" fill="#e8315a"/><path d="M5 3.5 8 6.5 5 9.5" fill="none" stroke="#fff" stroke-width="1.6"/></svg>
    </div>
  </div>
  <div class="tile t3" role="img" aria-label="Clip-on sunglasses with red lenses">
    <div class="band">Choose from the greatest variety of trends and class</div>
  </div>
  <div class="tile t4">
    <div class="photo" role="img" aria-label="Model lifting sunglasses over spectacles"></div>
    <div class="mark">Anselm</div>
    <div class="panel">High<br>Adrenaline<br><b>Eye</b><br>Protection</div>
  </div>
  <div class="tile t5" role="img" aria-label="Red frame on dark background">
    <div class="inner">
      <h3>SUPER SAVER</h3>
      <div class="sub">Prescription Glasses</div>
      <p>Choice of 10 frame styles available</p>
      <span class="btn">Book Now</span>
    </div>
  </div>
  <div class="tile t6">
    <div class="flat">FLAT</div>
    <div class="offer">
      <span class="num">50</span>
      <span class="stack"><span class="pc">%</span><span class="off">OFF</span></span>
    </div>
    <div class="word">SALE</div>
    <div class="days">ONLY FOR 4 DAYS</div>
  </div>
</section>

<footer class="site-footer abs">
  <h4 class="footer-h abs" style="left:126px;top:25px">Main Stuff</h4>
  <ul class="footer-links abs" style="left:127px;top:48px">
    <li>Home Page</li><li>Company</li><li>Collections</li><li>Glasses</li><li>Store</li><li>Blog</li><li>Contact</li>
  </ul>
  <h4 class="footer-h abs" style="left:213px;top:25px">Follow Us</h4>
  <div class="social abs"><i></i><i></i><i></i><i></i><i></i></div>
  <h4 class="footer-h abs" style="left:209px;top:93px">Subscribe to our Newsletter</h4>
  <div class="email abs">Your Email Address</div>
  <div class="submit abs">Submit</div>
  <div class="map abs" role="img" aria-label="Street map showing the shop location"></div>
  <div class="footer-rule abs"></div>
  <p class="copyright abs">Copyright 2013 anselmframes.com. Contact | Sitemap | Privacy Policy | Terms of use</p>
</footer>

</body>
</html>
```